Business Card Design

We are a project managment company specializing in Interior fitout
VRK is for Commercial, Domestic, Industial - we provide managment to these industries and see the projects through design to contruction
Would like an area on the back of the card where peoplr can write notes
Thinking laser lines and architectural finishes
Colour theme at the moment is light grey and red although im open to any colour/design scheme

VRK Ventures
Lewis Prentham
Managing Director
0419582147
lewis@vrkventures.com.au

```html
<!DOCTYPE html>
<html lang="en">
<head>
<meta charset="utf-8">
<title>VRK Ventures – Business Card</title>
<link rel="stylesheet" href="https://fonts.googleapis.com/css2?family=Cabin:wght@400;500&display=swap">
<style>
  :root {
    --page: #ecebe8;
    --card: #f1e7d3;
    --card-light: #f7f1e4;
    --navy: #323c4b;
    --rule: #8f8e88;
    --dot: #5c5f66;
    --shadow: rgba(40, 34, 24, 0.18);
  }
  * { box-sizing: border-box; margin: 0; padding: 0; }
  html, body {
    width: 1200px; height: 809px; overflow: hidden;
    background: var(--page);
    font-family: "Cabin", "Gill Sans", sans-serif;
    color: var(--navy);
  }
  .sheet {
    position: relative; width: 1200px; height: 809px;
    display: flex; align-items: center; justify-content: center; gap: 44px;
  }
  .card {
    position: relative; width: 520px; height: 318px;
    background: var(--card);
    box-shadow: 0 10px 28px var(--shadow);
    overflow: hidden;
  }
  /* front */
  .interior-photo {
    position: absolute; inset: 0;
    background:
      linear-gradient(115deg, rgba(255,255,255,0.55) 0%, rgba(255,255,255,0.15) 45%, rgba(255,255,255,0.5) 80%),
      linear-gradient(180deg, var(--card-light) 0%, var(--card) 100%);
  }
  .note-rules { position: absolute; left: 0; top: 0; }
  .brand {
    position: absolute; left: 34px; top: 78px;
    font-size: 27px; font-weight: 400; letter-spacing: 3px;
    color: var(--navy);
  }
  .dotted-rule {
    position: absolute; border-top: 2px dotted var(--dot);
  }
  .dotted-rule--upper { left: 22px; top: 126px; width: 220px; }
  .dotted-rule--lower { left: 22px; top: 292px; width: 476px; }
  .identity { position: absolute; left: 258px; top: 86px; }
  .identity__row { display: flex; align-items: center; gap: 10px; }
  .identity__name { font-size: 25px; font-weight: 400; letter-spacing: 0.5px; }
  .identity__role { font-size: 15px; margin: 2px 0 0 46px; }
  .contact {
    position: absolute; left: 112px; top: 168px;
    list-style: none; font-size: 17px;
  }
  .contact li { display: flex; align-items: center; gap: 10px; height: 30px; }
  .contact li:nth-child(2) { margin-left: -16px; }
  /* back */
  .back-rules { position: absolute; left: 0; top: 0; }
  .back-brand {
    position: absolute; right: 40px; top: 212px;
    font-size: 25px; letter-spacing: 3px; color: var(--navy);
  }
  .back-band {
    position: absolute; left: 0; right: 0; bottom: 30px; height: 40px;
    background: var(--navy);
  }
</style>
</head>
<body>
<main class="sheet">

  <section class="card card--front" aria-label="Card front">
    <div class="interior-photo" role="img" aria-label="Faded photograph of a bright commercial interior fitout"></div>
    <svg class="note-rules" width="520" height="80" aria-hidden="true">
      <g stroke="var(--rule)" stroke-width="1">
        <line x1="250" y1="14" x2="520" y2="14"/>
        <line x1="250" y1="32" x2="520" y2="32"/>
        <line x1="250" y1="50" x2="520" y2="50"/>
        <line x1="250" y1="68" x2="520" y2="68"/>
      </g>
    </svg>
    <div class="brand">VRK VENTURES</div>
    <div class="dotted-rule dotted-rule--upper"></div>
    <div class="identity">
      <div class="identity__row">
        <svg width="36" height="36" viewBox="0 0 36 36" aria-hidden="true">
          <circle cx="18" cy="18" r="16.5" fill="none" stroke="var(--navy)" stroke-width="1.6"/>
          <circle cx="18" cy="13" r="5" fill="var(--navy)"/>
          <path d="M9 27c0-5 4-8 9-8s9 3 9 8z" fill="var(--navy)"/>
        </svg>
        <span class="identity__name">Lewis Prentham</span>
      </div>
      <div class="identity__role">Managing Director</div>
    </div>
    <ul class="contact">
      <li>
        <svg width="28" height="22" viewBox="0 0 28 22" aria-hidden="true">
          <rect width="28" height="22" rx="2" fill="var(--navy)"/>
          <path d="M10 5c1 0 2 2 2 3s-1 1-1 2 2 3 3 3 1-1 2-1 3 1 3 2-1 3-3 3c-4 0-9-5-9-9 0-2 2-3 3-3z" fill="var(--card-light)"/>
        </svg>
        <span>0419582147</span>
      </li>
      <li>
        <svg width="28" height="22" viewBox="0 0 28 22" aria-hidden="true">
          <rect width="28" height="22" rx="2" fill="var(--navy)"/>
          <rect x="6" y="6" width="16" height="11" fill="none" stroke="var(--card-light)" stroke-width="1.4"/>
          <path d="M6 6l8 6 8-6" fill="none" stroke="var(--card-light)" stroke-width="1.4"/>
        </svg>
        <span>lewis@vrkventures.com.au</span>
      </li>
    </ul>
    <div class="dotted-rule dotted-rule--lower"></div>
  </section>

  <section class="card card--back" aria-label="Card back with notes area">
    <svg class="back-rules" width="520" height="250" aria-hidden="true">
      <g stroke="var(--rule)" stroke-width="1">
        <line x1="24" y1="24" x2="496" y2="24"/>
        <line x1="24" y1="50" x2="496" y2="50"/>
        <line x1="24" y1="76" x2="496" y2="76"/>
        <line x1="24" y1="102" x2="496" y2="102"/>
        <line x1="24" y1="128" x2="496" y2="128"/>
        <line x1="24" y1="154" x2="496" y2="154"/>
        <line x1="24" y1="180" x2="496" y2="180"/>
        <line x1="24" y1="206" x2="270" y2="206"/>
        <line x1="24" y1="232" x2="270" y2="232"/>
      </g>
    </svg>
    <div class="back-brand">VRK VENTURES</div>
    <div class="back-band"></div>
  </section>

</main>
</body>
</html>
```